Two (2) Merchant Advance Banner Ads

I need two (2) ads with rotating gif with 3 transitions for http://lendorbit.com/

Ad Specs:
Ad 1 must be an image equal to 250x250 pixels for website and email newsletter. .jpg, .gif, and
.png okay. No Flash!

Ad 2 must be an image equal to 720x90 pixels for website and mobile device view. .jpg, .gif, and
.png only. No Flash!

Client: Marlowe Funding Partners merchant cash advance company out of Chicago. They provide alternative (to a bank loan) financing for small business owners across the U.S.
Here's their website: www.marlowefp.com

Purpose: Recruit 3rd party sellers of alternative financing. There are many sales financing professionals already out there soliciting small businesses, we want them to make a decision to sell Marlowe's financing product to small businesses.

Copy:
Real People.
Competitive Commissions.
Great Rates.

I would like the logo (attached), phone number and CTA button to appear on all three transitions.
Call (888) 471-2859
Button: Get Started

Style:
Either something clean and simple, or something similar (not identifcal) to ads attached.
Brand standards guide is attached. Please use colors from guide.

```html
<!DOCTYPE html>
<html lang="en">
<head>
<meta charset="utf-8">
<title>Marlowe Funding Partners – Banner Ads</title>
<link href="https://fonts.googleapis.com/css2?family=Open+Sans:wght@400;600;700&family=Arimo:wght@400&display=swap" rel="stylesheet">
<style>
  :root {
    --lime: #b5c436;
    --white: #ffffff;
    --slate: #565b70;
    --ink: #111111;
    --suit: #2a2a2e;
    --canvas: #ffffff;
  }
  * { box-sizing: border-box; margin: 0; padding: 0; }
  html, body {
    width: 1200px; height: 1000px; overflow: hidden;
    background: var(--canvas);
    font-family: "Open Sans", Arial, sans-serif;
  }
  .stage { position: relative; width: 1200px; height: 1000px; }

  .ad { position: absolute; background: var(--lime); overflow: hidden; }
  .ad-square { left: 447px; top: 164px; width: 348px; height: 348px; }
  .ad-leaderboard { left: 55px; top: 633px; width: 1092px; height: 134px; }

  .ad-shapes { position: absolute; inset: 0; }

  .figure-slot {
    position: absolute;
    background: linear-gradient(180deg, #3a3a40 0%, var(--suit) 100%);
    border-radius: 30px 30px 0 0;
  }

  .brand-badge {
    position: absolute; border-radius: 50%;
    background: var(--white);
    display: flex; align-items: center; justify-content: center;
    text-align: center;
    color: var(--slate); font-weight: 600; line-height: 1.15;
  }

  .benefits { position: absolute; list-style: none; color: var(--slate); z-index: 2; }
  .benefits li { display: flex; align-items: flex-start; white-space: nowrap; }
  .benefits svg { flex: none; }

  .contact { position: absolute; text-align: center; font-family: "Arimo", Arial, sans-serif; color: var(--ink); }
  .contact .label { display: block; }

  .cta {
    position: absolute; background: var(--white); color: var(--slate);
    border-radius: 20px; font-weight: 700; letter-spacing: 0.06em;
    display: flex; align-items: center; justify-content: center;
    text-transform: uppercase;
  }

  /* square */
  .ad-square .figure-slot { left: 208px; top: 100px; width: 62px; height: 248px; }
  .ad-square .brand-badge { left: 248px; top: 153px; width: 100px; height: 100px; font-size: 12px; padding: 0 10px; }
  .ad-square .benefits { left: 28px; top: 63px; font-size: 19px; line-height: 27px; letter-spacing: -0.01em; }
  .ad-square .benefits li { margin-bottom: 6px; }
  .ad-square .benefits svg { width: 16px; height: 16px; margin: 6px 8px 0 0; }
  .ad-square .contact { left: 14px; top: 251px; width: 170px; }
  .ad-square .contact .label { font-size: 16px; line-height: 20px; }
  .ad-square .contact .number { font-size: 21px; line-height: 26px; }
  .ad-square .cta { left: 40px; top: 302px; width: 115px; height: 25px; font-size: 11px; }

  /* leaderboard */
  .ad-leaderboard .figure-slot { left: 35px; top: 10px; width: 112px; height: 124px; }
  .ad-leaderboard .brand-badge { left: 112px; top: 40px; width: 110px; height: 110px; font-size: 14px; padding: 0 12px 18px; }
  .ad-leaderboard .benefits { left: 303px; top: 14px; font-size: 24px; line-height: 33px; }
  .ad-leaderboard .benefits li { margin-bottom: 4px; }
  .ad-leaderboard .benefits svg { width: 19px; height: 19px; margin: 7px 9px 0 0; }
  .ad-leaderboard .contact { left: 680px; top: 36px; width: 224px; }
  .ad-leaderboard .contact .label { font-size: 20px; line-height: 22px; }
  .ad-leaderboard .contact .number { font-size: 28px; line-height: 32px; }
  .ad-leaderboard .cta { left: 913px; top: 52px; width: 152px; height: 33px; font-size: 14px; }
</style>
</head>
<body>
<div class="stage">

  <section class="ad ad-square" aria-label="Square banner ad, 250 by 250">
    <svg class="ad-shapes" width="348" height="348" viewBox="0 0 348 348" aria-hidden="true">
      <circle cx="108" cy="119" r="127" fill="none" stroke="var(--white)" stroke-width="3"/>
      <circle cx="108" cy="119" r="110" fill="var(--white)"/>
      <circle cx="346" cy="2" r="92" fill="none" stroke="var(--white)" stroke-width="3"/>
      <circle cx="346" cy="2" r="74" fill="var(--white)"/>
    </svg>
    <div class="figure-slot" role="img" aria-label="Illustration of a businessman in a dark suit looking through binoculars"></div>
    <div class="brand-badge">Marlowe Funding Partners</div>
    <ul class="benefits">
      <li><svg viewBox="0 0 16 16"><path d="M1.5 8.5 L6 13 L14.5 2.5" fill="none" stroke="var(--lime)" stroke-width="3" stroke-linecap="round" stroke-linejoin="round"/></svg>Real People</li>
      <li><svg viewBox="0 0 16 16"><path d="M1.5 8.5 L6 13 L14.5 2.5" fill="none" stroke="var(--lime)" stroke-width="3" stroke-linecap="round" stroke-linejoin="round"/></svg><span>Competitive<br>Commissions</span></li>
      <li><svg viewBox="0 0 16 16"><path d="M1.5 8.5 L6 13 L14.5 2.5" fill="none" stroke="var(--lime)" stroke-width="3" stroke-linecap="round" stroke-linejoin="round"/></svg>Great Rates</li>
    </ul>
    <div class="contact"><span class="label">Phone:</span><span class="number">(888) 471-2859</span></div>
    <div class="cta">Get Started</div>
  </section>

  <section class="ad ad-leaderboard" aria-label="Leaderboard banner ad, 720 by 90">
    <svg class="ad-shapes" width="1092" height="134" viewBox="0 0 1092 134" aria-hidden="true">
      <circle cx="0" cy="0" r="42" fill="none" stroke="var(--white)" stroke-width="3"/>
      <circle cx="0" cy="0" r="33" fill="var(--white)"/>
      <circle cx="460" cy="67" r="205" fill="none" stroke="var(--white)" stroke-width="3"/>
      <circle cx="460" cy="67" r="177" fill="var(--white)"/>
    </svg>
    <div class="figure-slot" role="img" aria-label="Illustration of a businessman in a dark suit looking through binoculars"></div>
    <div class="brand-badge">Marlowe Funding Partners</div>
    <ul class="benefits">
      <li><svg viewBox="0 0 16 16"><path d="M1.5 8.5 L6 13 L14.5 2.5" fill="none" stroke="var(--lime)" stroke-width="3" stroke-linecap="round" stroke-linejoin="round"/></svg>Real People</li>
      <li><svg viewBox="0 0 16 16"><path d="M1.5 8.5 L6 13 L14.5 2.5" fill="none" stroke="var(--lime)" stroke-width="3" stroke-linecap="round" stroke-linejoin="round"/></svg>Competitive Commissions</li>
      <li><svg viewBox="0 0 16 16"><path d="M1.5 8.5 L6 13 L14.5 2.5" fill="none" stroke="var(--lime)" stroke-width="3" stroke-linecap="round" stroke-linejoin="round"/></svg>Great Rates</li>
    </ul>
    <div class="contact"><span class="label">Phone:</span><span class="number">(888) 471-2859</span></div>
    <div class="cta">Get Started</div>
  </section>

</div>
</body>
</html>
```